Pediatric Practice Flyer Design

I need marketing flyer created for distribution. It is for a pediatric clinic. Need some realistic eye catching design and content. I already have a logo that will go on top of the flyer. I will be using corbelwade for flyer print service. So need it copyable for printing. Again, need eye catching content as well. We are planning on opening the clinic in December.

```html
<!DOCTYPE html>
<html lang="en">
<head>
<meta charset="utf-8">
<title>Maple Path Pediatrics – Coming Soon Flyer</title>
<link rel="stylesheet" href="https://fonts.googleapis.com/css2?family=Kaushan+Script&family=Oswald:wght@500&family=Roboto:wght@400;500;700&display=swap">
<style>
  :root{
    --orange:#ee8f22;
    --red:#e0252b;
    --blue:#1a6db5;
    --teal:#1a9e8f;
    --purple:#6a2c91;
    --ink:#1d1d1d;
    --paper:#ffffff;
    --mist:#e9e9e9;
  }
  *{margin:0;padding:0;box-sizing:border-box}
  html,body{width:1107px;height:1200px;overflow:hidden;background:var(--paper)}
  .flyer{position:relative;width:1107px;height:1200px;overflow:hidden;
    background:linear-gradient(180deg,var(--paper) 0%,var(--paper) 62%,var(--mist) 100%);
    font-family:"Roboto",Arial,sans-serif;color:var(--ink)}
  .layer{position:absolute;left:0;top:0;width:1107px;height:1200px}
  .brand{position:absolute;top:48px;left:0;width:100%;display:flex;justify-content:center;align-items:center;gap:14px}
  .brand-dot{width:34px;height:34px;border-radius:50%;background:var(--orange)}
  .brand-name{font-family:"Oswald",Arial,sans-serif;font-weight:500;font-size:44px;color:var(--red);letter-spacing:.5px}
  .inset-photo{position:absolute;left:726px;top:434px;width:284px;height:284px;border-radius:50%;
    border:7px solid var(--paper);
    background:radial-gradient(circle at 40% 45%,#d9a27c 0%,#6b4a6e 35%,#3a3a66 60%,#c9cbd6 100%)}
  .free-badge{position:absolute;left:72px;top:432px;width:200px;height:180px}
  .free-badge svg{position:absolute;inset:0}
  .free-text{position:absolute;left:0;top:30px;width:100%;text-align:center;color:var(--paper);
    font-family:"Oswald",Arial,sans-serif;font-weight:500;font-size:72px;line-height:1}
  .free-sub{position:absolute;left:0;top:110px;width:100%;text-align:center;color:var(--paper);
    font-weight:700;font-size:13px}
  .coming{position:absolute;left:104px;top:594px;font-family:"Kaushan Script",cursive;font-size:84px;line-height:1;color:var(--ink)}
  .headline{position:absolute;left:102px;top:692px;font-family:"Oswald",Arial,sans-serif;font-weight:500;
    font-size:122px;line-height:1.05;color:var(--red);letter-spacing:-1px}
  .subline{position:absolute;left:107px;top:820px;font-weight:500;font-size:37px;letter-spacing:.3px}
  .services{position:absolute;left:0;top:905px;width:100%;height:190px}
  .service{position:absolute;top:0;width:220px;margin-left:-110px;text-align:center}
  .service-icon{width:122px;height:122px;border-radius:50%;margin:0 auto;display:flex;align-items:center;justify-content:center}
  .service-icon svg{width:66px;height:66px}
  .service-label{margin-top:18px;font-weight:500;font-size:23px;line-height:1.2;text-transform:uppercase}
  .footer{position:absolute;left:0;top:1115px;width:100%;height:71px;background:var(--blue);color:var(--paper)}
  .footer-web{position:absolute;left:71px;top:10px;font-weight:700;font-size:25px}
  .footer-addr{position:absolute;left:71px;top:42px;font-size:18px}
  .footer-phone{position:absolute;left:666px;top:14px;font-size:18px}
  .footer-mail{position:absolute;left:666px;top:40px;font-size:18px}
  .base-strip{position:absolute;left:0;top:1186px;width:100%;height:14px;background:var(--mist)}
</style>
</head>
<body>
<main class="flyer">

  <svg class="layer" viewBox="0 0 778 1114" preserveAspectRatio="none" role="img" aria-label="Photo of a mother holding her baby while a smiling pediatrician examines the child in a clinic room">
    <defs>
      <linearGradient id="clinicPhoto" x1="0" y1="0" x2="1" y2="1">
        <stop offset="0" stop-color="#d8d6d2"/>
        <stop offset=".35" stop-color="#8f7aa8"/>
        <stop offset=".6" stop-color="#b9a48f"/>
        <stop offset="1" stop-color="#e4e2de"/>
      </linearGradient>
    </defs>
    <path d="M0,135 L705,135 C640,330 520,480 340,497 C230,500 120,450 0,375 Z" fill="url(#clinicPhoto)"/>
  </svg>

  <svg class="layer" viewBox="0 0 778 1114" preserveAspectRatio="none" aria-hidden="true">
    <rect x="0" y="0" width="778" height="8" fill="var(--orange)"/>
    <path d="M700,135 L778,135 L778,150 C710,330 570,480 330,499 C530,478 645,330 700,135 Z" fill="var(--red)"/>
    <path d="M778,195 C690,255 622,330 606,410" fill="none" stroke="var(--blue)" stroke-width="16"/>
    <path d="M778,228 C700,282 640,345 624,410 L700,648 L778,722 Z" fill="var(--orange)"/>
  </svg>

  <header class="brand">
    <span class="brand-dot"></span>
    <span class="brand-name">Maple Path Pediatrics</span>
  </header>

  <div class="inset-photo" role="img" aria-label="Photo of a doctor listening to a baby's chest with a stethoscope"></div>

  <div class="free-badge">
    <svg viewBox="0 0 200 180" aria-hidden="true">
      <g fill="var(--orange)">
        <circle cx="100" cy="90" r="68"/>
        <circle cx="100" cy="28" r="30"/>
        <circle cx="100" cy="152" r="30"/>
        <circle cx="40" cy="62" r="30"/>
        <circle cx="160" cy="62" r="30"/>
        <circle cx="44" cy="124" r="30"/>
        <circle cx="156" cy="124" r="30"/>
      </g>
    </svg>
    <div class="free-text">FREE</div>
    <div class="free-sub">1ST CONSULTATION</div>
  </div>

  <p class="coming">Coming Soon</p>
  <h1 class="headline">PEDIATRICIAN</h1>
  <p class="subline">ACCEPTING NEW PATIENTS</p>

  <section class="services">
    <div class="service" style="left:189px">
      <div class="service-icon" style="background:var(--teal)">
        <svg viewBox="0 0 24 24" fill="none" stroke="#fff" stroke-width="1.4" stroke-linecap="round" stroke-linejoin="round">
          <rect x="3" y="7" width="18" height="13" rx="2"/><path d="M9 7V5h6v2M12 10.5v6M9 13.5h6"/>
        </svg>
      </div>
      <p class="service-label">24/7<br>Service</p>
    </div>
    <div class="service" style="left:425px">
      <div class="service-icon" style="background:var(--red)">
        <svg viewBox="0 0 24 24" fill="none" stroke="#fff" stroke-width="1.4" stroke-linecap="round" stroke-linejoin="round">
          <path d="M9 17h6M3 17V11l3-4h4v10M10 6h10v11h-1"/><circle cx="7" cy="17.5" r="1.8"/><circle cx="17" cy="17.5" r="1.8"/><path d="M15 8.5v4M13 10.5h4M3 11h7"/>
        </svg>
      </div>
      <p class="service-label">Emergency<br>Service</p>
    </div>
    <div class="service" style="left:662px">
      <div class="service-icon" style="background:var(--purple)">
        <svg viewBox="0 0 24 24" fill="none" stroke="#fff" stroke-width="1.4" stroke-linecap="round" stroke-linejoin="round">
          <path d="M3 11l9-7 9 7M5 9.5V20h14V9.5M12 9v6M9 12h6"/><path d="M10 20v-3h4v3"/>
        </svg>
      </div>
      <p class="service-label">Good<br>Care</p>
    </div>
    <div class="service" style="left:899px">
      <div class="service-icon" style="background:var(--orange)">
        <svg viewBox="0 0 24 24" fill="none" stroke="#fff" stroke-width="1.4" stroke-linecap="round" stroke-linejoin="round">
          <path d="M6 3v5a4 4 0 0 0 8 0V3M10 12v3a4 4 0 0 0 8 0v-1"/><circle cx="18" cy="12" r="2"/>
        </svg>
      </div>
      <p class="service-label">Consultancy<br>Service</p>
    </div>
  </section>

  <footer class="footer">
    <p class="footer-web">www.maplepathpeds.com</p>
    <p class="footer-addr">48 Linden Row, Suite 12, Fairbrook NC 27000</p>
    <p class="footer-phone">Ph: 555-014-2837. Fax: 555-014-6190</p>
    <p class="footer-mail">office@maplepathpeds.com</p>
  </footer>
  <div class="base-strip"></div>

</main>
</body>
</html>
```